Heavy Equipment Rental Company Looking for Attractive Sign Design

We need a new sign for our forklift rental company in Southern California called Ridgeline Lift Outfitters. We also sell, service and move forklifts and other equipment, but forklift rentals are our main business. Our old sign on the street is deteriorating quickly. I've attached a photo of the old sign - it is approximately 52" high and 48" wide, but may be made 6" or so taller if needed. The old sign is included more to reference the information than the design - the old design definitely has issues (no ArtMarketry at the time). The smaller sign reading Pellworth dealer is not needed. We want the sign to be simple, clean and easy to read, but of course also attractive and professional. We would like the same information on it as is on the previous sign, but it may be re-arranged. The number 3100 is the street number. Here are the essential elements:
3100 (street number)
Ridgeline Lift Outfitters (business name)
714-382-6047 (phone)
www.ridgelineliftco.example (website)
Forklift Rentals and Sales (main businesses)
If possible, we would like the names of our 2 primary brands:
Pellworth and Varnecki Forklifts
Although, if there's no way to implement them nicely, then we can leave them off.

Target Market(s)

Industrial, Construction

Industry/Entity Type

Construction

Colors
0355a3

Requirements
Must have
• Bold, clean, easy to read, with the necessary information.
Nice to have
• Our main machines are all painted blue, so some blue in the design would be nice. In our industry, Pellworth forklifts and Varnecki forklifts are two different brands but have good reputations. It would be nice if we can include them in the design, although a nice design is more important than including the brand names.
Should not have
• Small or difficult to read text. Colors or fonts that are too playful.

```html
<!DOCTYPE html>
<html lang="en">
<head>
<meta charset="utf-8">
<title>Ridgeline Lift Outfitters – Street Sign</title>
<link rel="stylesheet" href="https://fonts.googleapis.com/css2?family=Bebas+Neue&family=Roboto:wght@900&display=swap">
<style>
  :root {
    --sign-blue: #343c8c;
    --sign-white: #ffffff;
    --backdrop: #d4d4d4;
    --icon-fill: #4a52a0;
  }
  html, body {
    margin: 0;
    padding: 0;
    width: 1200px;
    height: 970px;
    overflow: hidden;
    background: var(--backdrop);
  }
  .canvas {
    position: relative;
    width: 1200px;
    height: 970px;
  }
  .street-sign {
    position: absolute;
    left: 302px;
    top: 113px;
    width: 595px;
    height: 744px;
    display: block;
  }
  .sign-face { fill: var(--sign-blue); }
  .frame-line {
    fill: none;
    stroke: var(--sign-white);
    stroke-width: 6;
    stroke-linejoin: round;
    stroke-linecap: round;
  }
  .white-fill { fill: var(--sign-white); }
  .icon-area { fill: var(--icon-fill); }
  .street-number {
    font-family: "Roboto", Arial, sans-serif;
    font-weight: 900;
    font-size: 60px;
    fill: var(--sign-blue);
  }
  .name-text, .info-text, .brand-text {
    font-family: "Bebas Neue", "Oswald", sans-serif;
    fill: var(--sign-white);
  }
  .name-top { font-size: 89px; }
  .name-main { font-size: 145px; }
  .name-sub { font-size: 84px; }
  .web-address { font-size: 49px; }
  .services-line { font-size: 60px; fill: var(--sign-blue); }
  .phone-number { font-size: 72px; }
  .brand-text { font-size: 46px; }
</style>
</head>
<body>
<main class="canvas">
  <svg class="street-sign" viewBox="0 0 595 744" xmlns="http://www.w3.org/2000/svg" aria-label="Ridgeline Lift Outfitters street sign">
    <rect class="sign-face" x="0" y="0" width="595" height="744"/>

    <!-- upper frame -->
    <path class="frame-line" d="M22 116 V62 Q22 54 30 54 H204"/>
    <path class="frame-line" d="M390 54 H566 Q574 54 574 62 V116"/>

    <!-- street number plate -->
    <rect class="white-fill" x="204" y="20" width="186" height="69" rx="6"/>
    <text class="street-number" x="297" y="77" text-anchor="middle">3100</text>

    <!-- business name -->
    <text class="name-text name-top" x="297" y="204" text-anchor="middle" textLength="380" lengthAdjust="spacingAndGlyphs">RIDGELINE</text>
    <text class="name-text name-main" x="297" y="316" text-anchor="middle">LIFT</text>
    <path class="frame-line" d="M88 248 V328 H256"/>
    <path class="frame-line" d="M340 328 H506 V248"/>
    <rect class="icon-area" x="14" y="262" width="70" height="72" rx="4" role="img" aria-label="Forklift line icon facing right"/>
    <rect class="icon-area" x="512" y="262" width="70" height="72" rx="4" role="img" aria-label="Forklift line icon facing left"/>
    <text class="name-text name-sub" x="297" y="418" text-anchor="middle" textLength="404" lengthAdjust="spacing">OUTFITTERS</text>

    <!-- lower information frame -->
    <path class="frame-line" d="M22 428 V714 Q22 724 32 724 H564 Q574 724 574 714 V428"/>
    <text class="info-text web-address" x="297" y="478" text-anchor="middle" textLength="510" lengthAdjust="spacingAndGlyphs">WWW.RIDGELINELIFTCO.EXAMPLE</text>

    <rect class="white-fill" x="22" y="500" width="552" height="58"/>
    <text class="info-text services-line" x="298" y="547" text-anchor="middle" textLength="516" lengthAdjust="spacingAndGlyphs">FORKLIFT RENTALS AND SALES</text>

    <text class="info-text phone-number" x="302" y="627" text-anchor="middle" textLength="408" lengthAdjust="spacingAndGlyphs">714-382-6047</text>
    <line class="frame-line" x1="22" y1="638" x2="574" y2="638"/>

    <!-- brand names -->
    <text class="brand-text" x="160" y="698" text-anchor="middle">PELLWORTH</text>
    <text class="brand-text" x="424" y="698" text-anchor="middle">VARNECKI</text>
  </svg>
</main>
</body>
</html>
```